Brantley Gutters 15"x12" EDDM flyer

Brantley Gutter a new seamless gutter company is looking for designs for an Every Door Direct Mailing (EDDM) piece. The dimensions will be 15" long and 12" high. Designs must be submitted with pms colors and be at least 300 dpi.

Brantley Gutters LLC.
The products you need at prices you can afford!!!

Brantley Gutters provides an excellent rain gutter system to protect your property. Our “factory on wheels” will custom fit seamless gutters to your home. Our goal is quality craftsmanship with top-notch service at a competitive price. We take pride in our installations, have excellent customer service and guarantee our products and services.

15% off new gutter installations
$50 off gutter repair
$139.00 gutter clean out special. May be additional fee if more than 100 lf. Single story homes only
$99 and up for gutter tune ups. Reseal all end caps and seems, reattach down spouts and align gutters/downspouts

Telephone number: 904-RAINPRO 904-724-7776 I would like the number on there both ways.

Website: brantleygutters-demo.com

We would like a neat, clean design (nothing to busy). I like the color palate of red, white, blue and black.

I have a preference of not having to buy images. Main reason is after going I'll provide my own images.

residential single family homes

neat and clean that states what we do

• Some play on the BG in Brantley Gutters but must be professional. A lot of our clients will call because their wives no longer want them getting up on ladder.

```html
<!DOCTYPE html>
<html lang="en">
<head>
<meta charset="utf-8">
<title>Brantley Gutters LLC. EDDM Flyer</title>
<link rel="stylesheet" href="https://fonts.googleapis.com/css2?family=Michroma&family=Roboto+Condensed:ital,wght@0,700;1,700&family=Lato:wght@700;900&family=Oswald:wght@500&display=swap">
<style>
  :root {
    --navy: #0d1547;
    --navy-light: #1b2668;
    --red: #d2102b;
    --red-dark: #a90c21;
    --white: #ffffff;
    --paper: #f4f4f4;
    --paper-shade: #dedede;
    --grey: #5b5e63;
    --grey-light: #9a9da2;
    --ink: #111111;
    --page: #e6e6e6;
  }
  * { margin: 0; padding: 0; box-sizing: border-box; }
  html, body { width: 1200px; height: 900px; overflow: hidden; background: var(--page); }
  .flyer {
    position: absolute; left: 50px; top: 20px; width: 1100px; height: 860px;
    background: linear-gradient(180deg, var(--white) 0%, var(--paper) 55%, var(--paper-shade) 100%);
    overflow: hidden; box-shadow: 0 4px 14px rgba(0,0,0,.25);
  }
  .header {
    position: absolute; left: 0; top: 0; width: 1100px; height: 450px;
    background: linear-gradient(180deg, var(--navy) 0%, var(--navy-light) 100%);
    border-bottom: 5px solid var(--red);
  }
  .brand-name {
    position: absolute; top: 38px; width: 100%; text-align: center;
    font-family: "Michroma", sans-serif; font-weight: 400; font-size: 42px; line-height: 56px;
    color: var(--white); letter-spacing: 1px;
  }
  .tagline {
    position: absolute; top: 102px; width: 100%; text-align: center;
    font-family: "Roboto Condensed", sans-serif; font-weight: 700; font-size: 37px; line-height: 46px;
    color: var(--white); letter-spacing: 1.5px;
  }
  .header-rule { position: absolute; left: 0; top: 152px; width: 100%; height: 4px; background: var(--red); }
  .gallery {
    position: absolute; left: 24px; top: 162px; width: 1062px; height: 276px;
    background: linear-gradient(180deg, #6b6e73, #4a4d52);
    border-radius: 40px; border: 3px solid var(--grey-light);
  }
  .photo {
    position: absolute; top: 8px; height: 254px; border-radius: 26px; border: 3px solid var(--white);
  }
  .photo--guard { left: 8px; width: 350px; background: linear-gradient(135deg, #6f8a5c 0%, #3f4a58 55%, #2a3442 100%); }
  .photo--install { left: 364px; width: 340px; background: linear-gradient(160deg, #c7ccd2 0%, #8d9297 55%, #5e6267 100%); }
  .photo--downspout { left: 710px; width: 338px; background: linear-gradient(160deg, #d9ecf2 0%, #a66b4d 45%, #6e4330 100%); }

  .tab { position: absolute; top: 455px; height: 48px; }
  .tab svg { position: absolute; left: 0; top: 0; }
  .tab-label {
    position: absolute; left: 0; top: 6px; width: 100%; text-align: center;
    font-family: "Lato", sans-serif; font-weight: 900; font-size: 27px; line-height: 32px; color: var(--red);
  }
  .tab--offer { left: 20px; width: 220px; }
  .tab--about { left: 652px; width: 230px; }

  .offer { position: absolute; left: 0; }
  .offer-tag {
    position: absolute; top: 0; height: 100%;
    background: var(--navy); border-radius: 0 8px 8px 0;
    box-shadow: 2px 3px 4px rgba(0,0,0,.3); color: var(--white);
    font-family: "Roboto Condensed", sans-serif; font-style: italic; font-weight: 700;
    padding-left: 42px; white-space: nowrap;
  }
  .offer-price {
    position: absolute; left: 0; top: 0; height: 100%; background: var(--red);
    clip-path: polygon(0 0, calc(100% - 18px) 0, 100% 50%, calc(100% - 18px) 100%, 0 100%);
    color: var(--white); font-family: "Oswald", sans-serif; font-weight: 500;
    display: flex; align-items: center; justify-content: flex-end; padding-right: 24px;
  }
  .offer-price .amount { font-size: 28px; letter-spacing: -0.5px; }
  .offer-price .and-up { font-size: 16px; line-height: 15px; margin-left: 6px; text-align: center; }
  .offer-title { font-size: 16px; letter-spacing: .3px; }
  .offer-note { font-family: "Lato", sans-serif; font-style: normal; font-weight: 700; font-size: 12.5px; line-height: 14px; }
  .offer-note--small { font-size: 11px; line-height: 13px; }

  .offer--repair { top: 530px; width: 297px; height: 40px; }
  .offer--repair .offer-price { width: 145px; }
  .offer--repair .offer-tag { left: 115px; width: 182px; display: flex; align-items: center; }
  .offer--install { top: 595px; width: 380px; height: 42px; }
  .offer--install .offer-price { width: 145px; }
  .offer--install .offer-tag { left: 115px; width: 265px; display: flex; align-items: center; }
  .offer--clean { top: 658px; width: 435px; height: 56px; }
  .offer--clean .offer-price { width: 135px; }
  .offer--clean .offer-tag { left: 105px; width: 330px; padding-top: 4px; padding-left: 42px; }
  .offer--tune { top: 741px; width: 490px; height: 50px; }
  .offer--tune .offer-price { width: 165px; }
  .offer--tune .offer-tag { left: 135px; width: 355px; padding-top: 3px; padding-left: 42px; }

  .call-badge {
    position: absolute; left: 454px; top: 515px; width: 180px; height: 180px; border-radius: 50%;
    background: linear-gradient(160deg, #f7f7f7, #9ea1a6 60%, #d8d9db);
    box-shadow: 0 3px 6px rgba(0,0,0,.3);
  }
  .call-badge-inner {
    position: absolute; left: 12px; top: 12px; width: 156px; height: 156px; border-radius: 50%;
    background: radial-gradient(circle at 40% 35%, #e51a34, var(--red-dark));
    display: flex; flex-direction: column; align-items: center; justify-content: center;
    font-family: "Roboto Condensed", sans-serif; font-weight: 700; color: var(--white);
    font-size: 23px; line-height: 34px; white-space: nowrap;
  }

  .about-divider { position: absolute; left: 660px; top: 520px; width: 2px; height: 176px; background: var(--grey); }
  .about-text {
    position: absolute; left: 680px; top: 503px; width: 356px;
    font-family: "Lato", sans-serif; font-weight: 700; font-size: 17px; line-height: 26px;
    color: var(--ink); text-align: justify; hyphens: manual;
  }

  .footer-band { position: absolute; left: 0; top: 740px; width: 1100px; height: 120px; }
  .contact {
    position: absolute; right: 45px; color: var(--white);
    font-family: "Roboto Condensed", sans-serif; font-weight: 700;
    display: flex; align-items: center; gap: 8px; white-space: nowrap;
  }
  .contact--phone { top: 770px; font-size: 29px; line-height: 36px; }
  .contact--web { top: 806px; font-size: 20px; line-height: 26px; }
  .contact svg { flex: none; }
</style>
</head>
<body>
<main class="flyer">
  <header class="header">
    <h1 class="brand-name">BRANTLEY GUTTERS LLC.</h1>
    <p class="tagline">THE PRODUCTS YOU NEED AT PRICES YOU CAN AFFORD!!!</p>
    <div class="header-rule"></div>
    <div class="gallery">
      <div class="photo photo--guard" role="img" aria-label="Gloved hands fitting mesh gutter guard on a roof edge"></div>
      <div class="photo photo--install" role="img" aria-label="Installer fastening a seamless metal gutter under roof tiles"></div>
      <div class="photo photo--downspout" role="img" aria-label="Copper coloured gutter and downspout on a house eave"></div>
    </div>
  </header>

  <svg class="footer-band" viewBox="0 0 1100 120" preserveAspectRatio="none" aria-hidden="true">
    <path d="M0 54 L600 54 C640 54 650 28 690 28 L1100 28" fill="none" stroke="#9a9da2" stroke-width="5"/>
    <path d="M0 58 L600 58 C640 58 650 32 690 32 L1100 32 L1100 120 L0 120 Z" fill="#d2102b"/>
  </svg>

  <div class="tab tab--offer">
    <svg width="220" height="48" viewBox="0 0 220 48" aria-hidden="true">
      <path d="M0 0 H220 L196 46 H24 Z" fill="#b9bbbf"/>
      <path d="M4 0 H216 L194 43 H26 Z" fill="#ffffff"/>
    </svg>
    <span class="tab-label">WE OFFER</span>
  </div>
  <div class="tab tab--about">
    <svg width="230" height="48" viewBox="0 0 230 48" aria-hidden="true">
      <path d="M0 0 H230 L206 46 H24 Z" fill="#b9bbbf"/>
      <path d="M4 0 H226 L204 43 H26 Z" fill="#ffffff"/>
    </svg>
    <span class="tab-label">About Us</span>
  </div>

  <section class="offers">
    <div class="offer offer--repair">
      <div class="offer-tag"><span class="offer-title">gutter repair</span></div>
      <div class="offer-price"><span class="amount">$50 off</span></div>
    </div>
    <div class="offer offer--install">
      <div class="offer-tag"><span class="offer-title">new gutter installations</span></div>
      <div class="offer-price"><span class="amount">15% off</span></div>
    </div>
    <div class="offer offer--clean">
      <div class="offer-tag">
        <div class="offer-title">gutter clean out special</div>
        <div class="offer-note">May be additional fee if more than 100 lf.<br>Single story homes only</div>
      </div>
      <div class="offer-price"><span class="amount">$139</span></div>
    </div>
    <div class="offer offer--tune">
      <div class="offer-tag">
        <div class="offer-title">for gutter tune ups</div>
        <div class="offer-note offer-note--small">Reseal all end caps and seems, reattach down spouts<br>and align gutters/downspouts</div>
      </div>
      <div class="offer-price"><span class="amount">$99</span><span class="and-up">and<br>up</span></div>
    </div>
  </section>

  <div class="call-badge">
    <div class="call-badge-inner">
      <span>904-RAINPRO</span>
      <span>904-724-7776</span>
    </div>
  </div>

  <div class="about-divider"></div>
  <p class="about-text">Brantley Gutters provides an excellent rain gutter system to protect your property. Our “factory on wheels” will custom fit seamless gutters to your home. Our goal is quality craftsmanship with top-notch service at a competitive price. We take pride in our in&shy;stallations, have excellent customer service and guarantee our products and services.</p>

  <div class="contact contact--phone">
    <span>904-724-7776</span>
    <svg width="20" height="20" viewBox="0 0 24 24" aria-hidden="true"><circle cx="12" cy="12" r="10" fill="none" stroke="#fff" stroke-width="2"/><path d="M9 6c-1 1-2 3 0 6s4 5 6 6c1 0 2-1 2-2l-2-2-2 1c-1-1-2-2-3-4l1-2-2-3z" fill="#fff"/></svg>
  </div>
  <div class="contact contact--web">
    <span>www.brantleygutters-demo.com</span>
    <svg width="18" height="18" viewBox="0 0 24 24" aria-hidden="true"><circle cx="12" cy="12" r="10" fill="none" stroke="#fff" stroke-width="2"/><path d="M2 12h20M12 2c3 3 3 17 0 20M12 2c-3 3-3 17 0 20" fill="none" stroke="#fff" stroke-width="2"/></svg>
  </div>
</main>
</body>
</html>
```